Guiding the Evergreen Young Competitor:
A Family Roadmap for Nurturing Bold, Steady, and Resilient Daughters on Fields and Beyond.
📘 Book Cover Design Brief – “Guiding the Evergreen Young Competitor”

Project Title:
Design a bold, inspiring book cover for a best-selling book titled:
Guiding the Evergreen Young Competitor
Subtitle: A Family Roadmap for Nurturing Bold, Steady, and Resilient Daughters on Fields and Beyond

🎯 Audience:

Parents of female athletes ages 14–20 who want their daughters to build confidence, strength, resilience, and long-term success both in sports and in life.

This book should feel encouraging, empowering, and credible — NOT cheesy, childish, or overly academic.

📕 Design Tone & Style:

Powerful and professional — should feel like a best-selling book from a leading performance or parenting expert

Emotionally compelling — conveys hope, resilience, strength, and possibility

Visually modern and clean — avoid anything overly busy, cliché, or childish

Heroic/aspirational tone — think transformation, leadership, strong positioning

💡 Visual Direction / Ideas (Use as Inspiration, Not Limitation):

Strong, confident teenage female athlete imagery — adaptable beyond one specific sport

Symbolic visuals — e.g. athlete standing strong, on a starting line, looking bold into the future, silhouette, or power stance

Bold typography that feels clean and modern (e.g., Proxima Nova, Montserrat, Gotham, Bebas Neue, etc.)

A title that stands out clearly when viewed as a thumbnail on Bookvale

Color tones: Empowering, modern, and strong: think deep blues, greens, purples, or golds — avoid playful pastels or overly girly themes

Potential imagery: textured backgrounds, motion, bravery, development, strength, growth, sport/action overlays

🔥 What the Cover MUST Communicate:

✅ This is for parents who want strong, confident female athletes
✅ It’s a guidebook for personal development AND sports performance
✅ It’s about creating “UNSHAKEABLE” confidence — physically, mentally and emotionally
✅ The message is: You can help your daughter become her strongest, most confident self

📚 Back-of-Book Summary (for context):

"Guiding the Evergreen Young Competitor" is a parent's blueprint to building girls who are strong in body, confident in mind, and ready to lead on and off the field. Through simple strategies around strength training, mindset, nutrition, and character development, this book gives parents the tools to help their daughters stay injury-resistant, break through mental barriers, and unlock their full potential — in sports and in life.

✅ Deliverables:

Full cover design (front, back, spine) for paperback
High-resolution files (print-ready)
Source files (PSD, AI, etc.)
3D mockup versions of the book (standing, flat, stack)

Target Market(s)

Industry/Entity Type

Fitness

Font styles to use
Sans Serif

Colors
FFF300
FFF600
FEFA6F
FFFEC7
FFFEE8

Requirements
Must have
• Bold Font
Should not have
• I don't want an image of a female athlete. I want this to be font based.

```html
<!DOCTYPE html>
<html lang="en">
<head>
<meta charset="utf-8">
<title>Guiding the Evergreen Young Competitor — Full Cover</title>
<link rel="stylesheet" href="https://fonts.googleapis.com/css2?family=Bebas+Neue&family=Yellowtail&family=Saira+Extra+Condensed:ital,wght@1,700&display=swap">
<style>
  :root {
    --orange: #f39a1e;
    --orange-mid: #f6ad25;
    --glow: #f9e23a;
    --glow-soft: #fbec5a;
    --purple: #5a2a8c;
    --purple-deep: #33104f;
    --ink: #0d0a0a;
    --white: #ffffff;
    --photo-dark: #1c1a1a;
  }
  html, body {
    margin: 0;
    padding: 0;
    width: 1200px;
    height: 866px;
    overflow: hidden;
    background: var(--orange);
  }
  .cover {
    position: relative;
    width: 1200px;
    height: 866px;
    overflow: hidden;
    background:
      radial-gradient(ellipse 330px 320px at 880px 500px, var(--glow) 0%, rgba(249,226,58,0.55) 45%, rgba(249,226,58,0) 100%),
      radial-gradient(ellipse 300px 330px at 250px 430px, var(--glow-soft) 0%, rgba(251,236,90,0.4) 45%, rgba(251,236,90,0) 100%),
      linear-gradient(180deg, var(--orange-mid), var(--orange));
    font-family: Arial, Helvetica, sans-serif;
  }
  .back-blurb {
    position: absolute;
    left: 81px;
    top: 154px;
    width: 424px;
    margin: 0;
    font-weight: 700;
    font-size: 12.6px;
    line-height: 16.6px;
    color: var(--purple-deep);
    text-align: justify;
    text-align-last: center;
  }
  .back-rule {
    position: absolute;
    left: 161px;
    top: 297px;
    width: 268px;
    height: 5px;
    background: var(--purple-deep);
  }
  .author-photo {
    position: absolute;
    left: 206px;
    top: 324px;
    width: 173px;
    height: 217px;
    box-sizing: border-box;
    border: 3px solid var(--white);
    background: radial-gradient(ellipse at 50% 40%, #3a3533, var(--photo-dark) 70%);
    box-shadow: 0 1px 3px rgba(0,0,0,0.35);
  }
  .author-bio {
    position: absolute;
    left: 113px;
    top: 552px;
    width: 363px;
    margin: 0;
    font-weight: 700;
    font-size: 10.6px;
    line-height: 14.2px;
    color: var(--purple-deep);
    text-align: justify;
    text-align-last: center;
  }
  .spine, .front-title {
    position: absolute;
    left: 0;
    top: 0;
  }
  .title-text { font-family: "Bebas Neue", Impact, sans-serif; }
  .title-purple { fill: var(--purple); }
  .title-ink { fill: var(--ink); }
  .title-script {
    font-family: "Yellowtail", cursive;
    fill: var(--ink);
  }
  .cover-art {
    position: absolute;
    left: 800px;
    top: 440px;
    width: 210px;
    height: 236px;
    border-radius: 40% 40% 8px 8px;
    background: radial-gradient(ellipse at 50% 60%, rgba(138,47,196,0.35), rgba(138,47,196,0.08) 60%, rgba(138,47,196,0) 80%);
  }
  .subtitle {
    position: absolute;
    left: 680px;
    top: 686px;
    width: 470px;
    margin: 0;
    font-family: "Saira Extra Condensed", "Arial Narrow", sans-serif;
    font-style: italic;
    font-weight: 700;
    font-size: 21px;
    line-height: 23px;
    color: var(--purple-deep);
    text-align: center;
    text-transform: uppercase;
  }
  .author-name {
    position: absolute;
    left: 680px;
    top: 762px;
    width: 470px;
    margin: 0;
    font-family: "Bebas Neue", Impact, sans-serif;
    font-size: 50px;
    line-height: 50px;
    color: var(--purple);
    text-align: center;
    letter-spacing: 1px;
  }
</style>
</head>
<body>
<main class="cover">

  <section class="back-cover">
    <p class="back-blurb">"Guiding the Evergreen Young Competitor" is a parent's blueprint to building girls who are strong in body, confident in mind, and ready to lead on and off the field. Through simple strategies around strength training, mindset, nutrition, and character development, this book gives parents the tools to help their daughters stay injury-resistant, break through mental barriers, and unlock their full potential — in sports and in life.</p>
    <div class="back-rule"></div>
    <div class="author-photo" role="img" aria-label="Author portrait photograph on a dark background"></div>
    <p class="author-bio">Dorian has 15 years experience, specializing in Personal Training and Sport Performance. He focuses his training on creating programs that improve performance and reduce the risk of injury. Dorian has worked with clients from 8 – 73. He is a 2 Time Bookvale best-selling author with Rise Steady Now and Fuel Smart for Varsity Athletes. Dorian commits his life to coaching each client to RISE STEADY. Stridewell Fitness was born out of his passion to make each person who walks in the door the very best version of themselves.</p>
  </section>

  <svg class="spine" width="1200" height="866" viewBox="0 0 1200 866" aria-label="Spine">
    <text class="title-text title-purple" x="159" y="-591" font-size="25" textLength="336" lengthAdjust="spacingAndGlyphs" transform="rotate(90)">GUIDING THE EVERGREEN YOUNG COMPETITOR</text>
    <text class="title-text title-purple" x="540" y="-591" font-size="25" textLength="116" lengthAdjust="spacingAndGlyphs" transform="rotate(90)">DORIAN HALVICK</text>
  </svg>

  <svg class="front-title" width="1200" height="866" viewBox="0 0 1200 866" aria-label="Guiding the Evergreen Young Competitor">
    <text class="title-script" x="678" y="168" font-size="40">the</text>
    <text class="title-text title-purple" x="788" y="169" font-size="105" textLength="238" lengthAdjust="spacingAndGlyphs">GUIDING</text>
    <text class="title-text title-ink" x="679" y="262" font-size="117" textLength="458" lengthAdjust="spacingAndGlyphs">EVERGREEN</text>
    <text class="title-text title-purple" x="791" y="347" font-size="106" textLength="233" lengthAdjust="spacingAndGlyphs">YOUNG</text>
    <text class="title-text title-ink" x="782" y="434" font-size="102" textLength="250" lengthAdjust="spacingAndGlyphs">COMPETITOR</text>
  </svg>

  <div class="cover-art" role="img" aria-label="Illustration of a figure in a yoga warrior pose in purple tones"></div>

  <p class="subtitle">A Family Roadmap for Nurturing Bold, Steady, and Resilient Daughters on Fields and Beyond</p>
  <p class="author-name">DORIAN HALVICK</p>

</main>
</body>
</html>
```